Bright Fern Accounting Postcard

I need a postcard that highlights my services and contact info. Please use the website for graphics/info... www.BrightFernAccounting.com

Target Market(s)

Business owners

Industry/Entity Type

Bookkeeper

Colors

Designer to choose colors to be used in the design.

Requirements
Must have
• Services listed, Certified Ledgerly Online Pro Advisor (can add Ledgerly logo), Contact info

```html
<!DOCTYPE html>
<html lang="en">
<head>
<meta charset="utf-8">
<title>Bright Fern Accounting Postcard</title>
<link href="https://fonts.googleapis.com/css2?family=Noto+Serif:wght@700&family=PT+Sans:wght@400;700&display=swap" rel="stylesheet">
<style>
:root{
  --navy:#1a3a6b;
  --navy-deep:#0f2d5e;
  --panel:rgba(30,64,120,.93);
  --grey:#6d6e71;
  --grey-light:#8a8b8e;
  --green:#2ca01c;
  --line:#8fa3a6;
  --bg:#cccccc;
  --white:#ffffff;
}
*{margin:0;padding:0;box-sizing:border-box}
html,body{width:963px;height:1200px;overflow:hidden;background:var(--bg)}
body{position:relative;font-family:"PT Sans",sans-serif}
.card{position:absolute;left:82px;width:799px;background:var(--white);overflow:hidden;box-shadow:8px 8px 10px rgba(0,0,0,.25)}
.card--front{top:53px;height:532px}
.card--back{top:623px;height:537px}

.brand{position:absolute;display:flex;align-items:center;gap:10px;font-family:"Noto Serif",serif;font-weight:700;color:var(--navy-deep);white-space:nowrap}
.brand__mark{background:var(--navy-deep)}
.card--front .brand{left:0;right:0;top:26px;justify-content:center;font-size:38px}
.card--front .brand__mark{width:34px;height:34px}
.card--back .brand{left:38px;top:34px;font-size:24px}
.card--back .brand__mark{width:22px;height:22px}

.photo{position:absolute;left:0;top:103px;width:799px;height:352px;background:linear-gradient(100deg,#3a4a66 0%,#6b7a90 45%,#c9c2b8 70%,#8a8e96 100%)}
.panel{position:absolute;left:0;top:103px;width:799px;height:352px}
.services{position:absolute;left:0;top:103px;width:460px;height:352px;color:var(--white)}
.service{position:absolute;left:26px;display:flex;gap:18px}
.service svg{width:58px;height:58px;flex:none;margin-top:20px}
.service h2{font-weight:400;font-size:14.5px;letter-spacing:.2px;line-height:1.1}
.service p{font-size:11.2px;line-height:1.33;width:284px;text-align:justify}
.service--1{top:27px}.service--2{top:150px}.service--3{top:258px}

.footer{position:absolute;left:0;width:799px;height:78px}
.card--front .footer{top:455px}
.card--back .footer{top:459px}
.footer svg.band{position:absolute;inset:0;width:100%;height:100%}
.phone{position:absolute;left:24px;top:13px;display:flex;align-items:center;gap:12px;color:var(--white);font-weight:700;font-size:24px}
.phone svg{width:48px;height:48px}
.web{position:absolute;left:312px;top:10px;color:var(--white)}
.web__site{font-weight:700;font-size:22.5px;line-height:1.3}
.web__mail{font-size:20.5px;line-height:1.4}
.partner{position:absolute;width:98px;height:98px;border-radius:50%;background:var(--green)}
.card--front .partner{left:690px;top:411px}
.card--back .partner{left:691px;top:414px}

.list{position:absolute;left:52px;color:var(--navy);font-size:14.5px;display:flex;align-items:center;gap:22px}
.list svg{width:58px;height:48px}
.list--1{top:125px}.list--2{top:238px}.list--3{top:364px}
.stamp{position:absolute;left:632px;top:59px;width:108px;height:143px;border:1.2px solid var(--line)}
.postmark{position:absolute;left:476px;top:100px;width:180px;height:80px}
.address{position:absolute;left:436px;width:302px;height:1.2px;background:var(--line)}
</style>
</head>
<body>

<svg width="0" height="0" style="position:absolute">
  <defs>
    <symbol id="icon-coins" viewBox="0 0 60 50"><g fill="none" stroke="currentColor" stroke-width="2.4"><circle cx="16" cy="30" r="12"/><path d="M16 22v16M20 25c-2-2-8-2-8 1s8 2 8 6-6 3-8 1"/><ellipse cx="40" cy="10" rx="12" ry="4"/><path d="M28 10v8c0 2 5 4 12 4s12-2 12-4v-8M28 18v8c0 2 5 4 12 4s12-2 12-4v-8"/><ellipse cx="44" cy="32" rx="12" ry="4"/><path d="M32 32v10c0 2 5 4 12 4s12-2 12-4V32"/></g></symbol>
    <symbol id="icon-report" viewBox="0 0 60 60"><g fill="none" stroke="currentColor" stroke-width="2.4"><rect x="6" y="6" width="36" height="50"/><rect x="18" y="2" width="12" height="7"/><circle cx="16" cy="20" r="5"/><path d="M26 17h10M26 22h10M12 30h14M12 35h10M12 52V46M17 52V42M22 52V38M27 52V44"/><circle cx="44" cy="42" r="11"/><path d="M44 31v11h11"/></g></symbol>
    <symbol id="icon-team" viewBox="0 0 70 50"><g fill="none" stroke="currentColor" stroke-width="2.4"><circle cx="12" cy="8" r="5"/><circle cx="35" cy="8" r="5"/><circle cx="58" cy="8" r="5"/><path d="M5 26c0-8 14-8 14 0M28 26c0-8 14-8 14 0M51 26c0-8 14-8 14 0M2 30h66M8 30v18M62 30v18M35 30v18M2 20v28M68 20v28"/></g></symbol>
    <symbol id="icon-phone" viewBox="0 0 48 48"><circle cx="24" cy="24" r="22" fill="none" stroke="currentColor" stroke-width="2.5"/><path d="M16 13l5 0 2 6-3 3c2 4 4 6 8 8l3-3 6 2v5c-1 2-3 2-5 2-10-2-17-9-18-19 0-2 0-3 2-4z" fill="currentColor"/></symbol>
  </defs>
</svg>

<section class="card card--front">
  <div class="brand"><span class="brand__mark"></span>Bright Fern Accounting</div>
  <div class="photo" role="img" aria-label="Photo of business people reviewing documents at an office table"></div>
  <svg class="panel" viewBox="0 0 799 352" preserveAspectRatio="none"><polygon points="0,0 402,0 442,352 0,352" fill="var(--panel)"/></svg>
  <div class="services">
    <div class="service service--1"><svg><use href="#icon-coins"/></svg><div><h2>BOOKKEEPING</h2><p>Let us take over the day to day bookkeeping so you can get back to running your business. We offer Ledgerly Online setup and ongoing bookkeeping, including daily journal entries, accounts payables &amp; receivables, bill pay, sales tax reporting &amp; payments, account reconciliation, and more.</p></div></div>
    <div class="service service--2"><svg><use href="#icon-report"/></svg><div><h2>FINANCIAL REPORTING</h2><p>We'll provide easy to understand financial reports that allow you and your team to manage cash flow, create budgets and make forecasting decisions. Want real time data? Let us provide solutions with the latest in mobile apps and dashboards.</p></div></div>
    <div class="service service--3"><svg><use href="#icon-team"/></svg><div><h2>PAYROLL PROCESSING</h2><p>Whether you have 5 employees or 100+, payroll can be an overwhelming and time consuming task. We offer full service payroll processing, including employee on boarding and reporting.</p></div></div>
  </div>
  <div class="footer">
    <svg class="band" viewBox="0 0 799 78" preserveAspectRatio="none"><rect width="799" height="78" fill="var(--navy)"/><path d="M0 0H630C665 0 682 40 682 78H0Z" fill="var(--grey-light)"/></svg>
    <div class="phone"><svg><use href="#icon-phone"/></svg>1.877.555.0142</div>
    <div class="web"><div class="web__site">brightfernaccounting.com</div><div class="web__mail">info@brightfernaccounting.com</div></div>
  </div>
  <div class="partner" aria-label="Ledgerly partner badge"></div>
</section>

<section class="card card--back">
  <div class="brand"><span class="brand__mark"></span>Bright Fern Accounting</div>
  <div class="list list--1"><svg><use href="#icon-coins"/></svg>BOOKKEEPING</div>
  <div class="list list--2"><svg><use href="#icon-report"/></svg>FINANCIAL REPORTING</div>
  <div class="list list--3"><svg><use href="#icon-team"/></svg>PAYROLL PROCESSING</div>
  <svg class="postmark" viewBox="0 0 180 80" fill="none" stroke="var(--line)" stroke-width="1.3"><path d="M2 30C40 0 90 10 120 30S170 40 178 25M2 45C40 15 90 25 120 45S170 55 178 40M2 60C40 30 90 40 120 60S170 70 178 55"/></svg>
  <div class="stamp"></div>
  <div class="address" style="top:292px"></div>
  <div class="address" style="top:333px"></div>
  <div class="address" style="top:374px"></div>
  <div class="address" style="top:415px"></div>
  <div class="footer">
    <svg class="band" viewBox="0 0 799 78" preserveAspectRatio="none"><rect width="799" height="78" fill="var(--grey)"/><path d="M0 0H630C665 0 682 40 682 78H0Z" fill="var(--navy-deep)"/></svg>
    <div class="phone"><svg><use href="#icon-phone"/></svg>1.877.555.0142</div>
    <div class="web"><div class="web__site">brightfernaccounting.com</div><div class="web__mail">info@brightfernaccounting.com</div></div>
  </div>
  <div class="partner" aria-label="Ledgerly partner badge"></div>
</section>

</body>
</html>
```